Kindle Thread Pty Ltd Brochure and New Image Design

Initally we will be needing a A4 Folder design created as well as a Template for a Double Sided Flyer. We need a cutting edge design which we can incorporate into a Brochure, Flyer Handout, Website etc. Basically we are re-branding our company starting with an "About Us" Folder which we will be distributing to potential customers.
We are an Embroidery company that caters for mid-large companies dealing with clothing ranging from Corporate Attire to Workwear. Our current website has more information on what we do and you can use that as a valid reference point (www.kindlethread.com.au), However the website will be step 2 in freshening up our image.
Our company has been thriving over the 20 years we have been in business by supplying a higher quality product as well as Service that is second to none, unfortunately our branding image has been overlooked while we have spent more time/effort on our customer service.
We have used the colours Maroon (PMS 216C) Silver Grey (PMS Cool Gray 7) White and Black. We would like to maintain these colours but incorporate them together in a way that has a more "modern edgey" look.
Target Market(s)
Purchasing / Marketing Officers of Mid-Large Corporate Companies.
Industry/Entity Type
Clothing
Look and feel

```html
<!DOCTYPE html>
<html lang="en">
<head>
<meta charset="utf-8">
<title>Kindle Thread Embroidery – Folder Cover</title>
<link rel="stylesheet" href="https://fonts.googleapis.com/css2?family=Baloo+2:wght@500;700;800&family=Inter:wght@200;300&display=swap">
<style>
  :root {
    --maroon: #86204c;
    --silver: #a6a7a9;
    --silver-light: #b4b5b7;
    --white: #ffffff;
    --stone-light: #c8c4bc;
    --stone-mid: #a7a39c;
    --stone-dark: #7d7a75;
    --navy: #1c2748;
    --navy-soft: #2f3b63;
    --cream: #e8dfd9;
    --cream-shade: #cfc4bd;
    --shadow: rgba(20, 22, 34, 0.55);
  }
  * { margin: 0; padding: 0; box-sizing: border-box; }
  html, body { width: 1200px; height: 776px; overflow: hidden; background: var(--white); }
  .cover { position: relative; width: 1200px; height: 776px; overflow: hidden; }

  .hero-photo {
    position: absolute; left: 0; top: 0; width: 1200px; height: 576px;
    background:
      linear-gradient(180deg, rgba(20,22,34,0) 0%, rgba(20,22,34,0) 55%, var(--shadow) 100%),
      linear-gradient(90deg,
        var(--stone-mid) 0%,
        var(--stone-dark) 6%,
        var(--navy-soft) 14%,
        var(--navy) 28%,
        var(--navy) 44%,
        var(--navy-soft) 50%,
        var(--cream) 56%,
        var(--cream-shade) 62%,
        var(--navy) 66%,
        var(--cream) 72%,
        var(--cream) 84%,
        var(--navy) 87%,
        var(--cream-shade) 92%,
        var(--stone-mid) 96%,
        var(--stone-light) 100%);
  }
  .hero-photo::before {
    content: ""; position: absolute; left: 0; top: 0; width: 1200px; height: 260px;
    background: linear-gradient(180deg, var(--stone-light) 0%, rgba(200,196,188,0.85) 45%, rgba(200,196,188,0) 100%);
  }
  .hero-headline {
    position: absolute; left: 101px; top: 468px;
    font-family: "Inter", sans-serif; font-weight: 300;
    font-size: 38px; line-height: 37px; letter-spacing: 0.2px;
    color: var(--white); text-transform: uppercase;
  }

  .brand-band {
    position: absolute; left: 0; top: 576px; width: 1200px; height: 200px;
    background: linear-gradient(180deg, var(--silver-light), var(--silver));
  }
  .brand-mark {
    position: absolute; left: 54px; top: 604px; width: 228px; height: 120px;
    border: 2px solid var(--maroon); border-radius: 6px;
    display: flex; align-items: center; justify-content: center;
    font-family: "Baloo 2", sans-serif; font-weight: 800;
    font-size: 30px; color: var(--maroon);
  }
  .brand-name {
    position: absolute; left: 307px; top: 615px;
    font-family: "Baloo 2", sans-serif; font-weight: 800;
    font-size: 42px; line-height: 46px; color: var(--maroon);
  }
  .brand-rule {
    position: absolute; left: 307px; top: 671px; width: 893px; height: 1px;
    background: var(--maroon);
  }
  .brand-tagline {
    position: absolute; left: 307px; top: 679px;
    font-family: "Inter", sans-serif; font-weight: 200;
    font-size: 22px; color: var(--white);
  }

  .contact {
    position: absolute; left: 934px; top: 606px;
    font-family: "Baloo 2", sans-serif; font-weight: 500; font-style: normal;
    font-size: 13px; line-height: 19px; color: var(--white);
  }
  .contact .label, .contact .company { color: var(--maroon); font-weight: 700; }
  .contact .lines { margin-bottom: 18px; }
</style>
</head>
<body>
  <main class="cover">
    <div class="hero-photo" role="img" aria-label="Photograph of a smiling man in a navy fleece and a woman in a cream fleece with navy scarf, seated against a grey stone wall"></div>
    <h1 class="hero-headline">Custom Uniform &amp;<br>Embroidery Specialists!</h1>

    <section class="brand-band"></section>
    <div class="brand-mark">Kindle Thread</div>
    <h2 class="brand-name">Kindle Thread</h2>
    <div class="brand-rule"></div>
    <p class="brand-tagline">Embroidery</p>

    <address class="contact">
      <div class="lines">
        <div class="company">Kindle Thread Embroidery P/L</div>
        <div>22-30 Harrow Lane</div>
        <div>Ridgefield NSW 2999 AUSTRALIA</div>
      </div>
      <div><span class="label">Phone:</span> +612 9000 4410</div>
      <div><span class="label">Facsimile:</span> +612 9000 4411</div>
      <div>enquiries@kindlethread.com.au</div>
    </address>
  </main>
</body>
</html>
```